Mabel's Fitness Business Cards

I would like my business cards to look expensive and sophisticated using my logo and the information below.

FRONT
Mabel’s Fitness logo

Tag line Become your happiest, healthiest and strongest self

Mabel Quint Harlow
Personal Trainer

e. mabel@mabelsfitstudio.example

t. 0781530462

w. www.mabelsfitstudio.example

```html
<!DOCTYPE html>
<html lang="en">
<head>
<meta charset="UTF-8">
<title>Mabel's Fitness Business Cards</title>
<link href="https://fonts.googleapis.com/css2?family=Jost:wght@400;500;600&display=swap" rel="stylesheet">
<style>
  :root {
    --backdrop: #e8e3dc;
    --paper: #ffffff;
    --teal: #3fb0bd;
    --cocoa: #5a4a45;
    --taupe: #a3918a;
    --ink-soft: #5f5451;
    --shadow: rgba(60, 45, 35, 0.18);
  }
  * { box-sizing: border-box; margin: 0; padding: 0; }
  html, body {
    width: 1200px;
    height: 800px;
    overflow: hidden;
    background: var(--backdrop);
    font-family: "Jost", "Helvetica Neue", Arial, sans-serif;
  }
  .sheet {
    width: 1200px;
    height: 800px;
    display: flex;
    align-items: center;
    justify-content: center;
    gap: 60px;
  }
  .card {
    position: relative;
    width: 540px;
    height: 315px;
    background: var(--paper);
    border-radius: 4px;
    box-shadow: 0 10px 30px var(--shadow);
    overflow: hidden;
  }

  /* Brand side */
  .card--brand {
    display: flex;
    flex-direction: column;
    align-items: center;
  }
  .brand-mark {
    margin-top: 62px;
    width: 74px;
    height: 74px;
    border: 5px solid var(--taupe);
    border-radius: 50%;
  }
  .brand-name {
    margin-top: 18px;
    color: var(--teal);
    font-weight: 400;
    font-size: 30px;
    letter-spacing: 0.22em;
    text-transform: uppercase;
  }
  .tagline {
    position: absolute;
    bottom: 34px;
    left: 0;
    right: 0;
    text-align: center;
    color: var(--ink-soft);
    font-size: 16px;
    letter-spacing: 0.02em;
  }

  /* Contact side */
  .card-art {
    position: absolute;
    inset: 0;
  }
  .holder {
    position: absolute;
    top: 26px;
    left: 30px;
  }
  .holder-name {
    color: var(--paper);
    font-weight: 600;
    font-size: 23px;
    line-height: 1.1;
  }
  .holder-role {
    color: var(--cocoa);
    font-weight: 400;
    font-size: 18px;
    margin-top: 2px;
  }
  .contact-list {
    position: absolute;
    left: 28px;
    top: 190px;
    list-style: none;
  }
  .contact-item {
    display: flex;
    align-items: center;
    gap: 9px;
    color: var(--paper);
    font-size: 15px;
    line-height: 26px;
    white-space: nowrap;
  }
  .contact-icon {
    width: 14px;
    height: 14px;
    flex: none;
  }
  .side-name {
    position: absolute;
    left: 300px;
    top: 0;
    width: 220px;
    height: 315px;
    display: flex;
    align-items: center;
    justify-content: center;
    color: var(--teal);
    font-weight: 400;
    font-size: 18px;
    letter-spacing: 0.16em;
    text-transform: uppercase;
    white-space: nowrap;
  }
</style>
</head>
<body>
<main class="sheet">

  <section class="card card--brand">
    <div class="brand-mark"></div>
    <div class="brand-name">Mabel’s Fitness</div>
    <p class="tagline">Become your happiest, healthiest and strongest self</p>
  </section>

  <section class="card card--contact">
    <svg class="card-art" viewBox="0 0 540 315" width="540" height="315" aria-hidden="true">
      <rect width="540" height="315" fill="var(--teal)"/>
      <circle cx="90" cy="385" r="252" fill="var(--cocoa)"/>
      <circle cx="440" cy="158" r="165" fill="var(--paper)"/>
    </svg>

    <div class="holder">
      <div class="holder-name">Mabel Quint Harlow</div>
      <div class="holder-role">Personal Trainer</div>
    </div>

    <ul class="contact-list">
      <li class="contact-item">
        <svg class="contact-icon" viewBox="0 0 16 16"><path d="M4 1.5 6.2 4.6 4.8 6.3c.9 2 2.5 3.6 4.6 4.6l1.6-1.4 3.1 2.2-1 2.4C7.6 14 2 8.4 1.6 2.6Z" fill="var(--teal)"/></svg>
        <span>078 153 0462</span>
      </li>
      <li class="contact-item">
        <svg class="contact-icon" viewBox="0 0 16 16"><rect x="1" y="3" width="14" height="10" rx="1" fill="var(--teal)"/><path d="M1.5 3.8 8 9l6.5-5.2" fill="none" stroke="var(--cocoa)" stroke-width="1.3"/></svg>
        <span>mabel@mabelsfitstudio.example</span>
      </li>
      <li class="contact-item">
        <svg class="contact-icon" viewBox="0 0 16 16"><circle cx="8" cy="8" r="7" fill="var(--teal)"/><g fill="none" stroke="var(--cocoa)" stroke-width="1"><ellipse cx="8" cy="8" rx="3" ry="7"/><path d="M1 8h14M2.2 4.5h11.6M2.2 11.5h11.6"/></g></svg>
        <span>mabelsfitstudio.example</span>
      </li>
    </ul>

    <div class="side-name">Mabel’s Fitness</div>
  </section>

</main>
</body>
</html>
```